Business Card Design Project

I am looking for a business card that includes the logo that I am uploading. It is an Interior Design business. This card must include the following (in addition to the logo):
Lena Vart
Interior Designer - Allied Member, NPDG
4213 Willowmere Lane
Linden Falls, MN 55990
612-555-0187
lenapvart@orbimail.test
lenavartspaces.test

Industry/Entity Type

Business

Requirements
Must have
• This card must include the following (in addition to the logo):
Lena Vart
4213 Willowmere Lane
Linden Falls, MN 55990
612-555-0187
lenapvart@orbimail.test
lenavartspaces.test

```html
<!DOCTYPE html>
<html lang="en">
<head>
<meta charset="utf-8">
<title>Lena Vart Spaces – Business Card</title>
<link rel="stylesheet" href="https://fonts.googleapis.com/css2?family=Arimo:wght@400&family=Oswald:wght@300&family=Reenie+Beanie&display=swap">
<style>
  :root {
    --page-bg: #ececec;
    --card-bg: #ffffff;
    --card-edge: #cfcfcf;
    --ink-brown: #4a3b26;
    --accent-orange: #f28a1c;
    --pattern-orange: #fcc48f;
    --note-ink: #555555;
    --art-fill: #f3eee7;
  }
  * { margin: 0; padding: 0; box-sizing: border-box; }
  html, body { width: 1200px; height: 900px; overflow: hidden; }
  body { background: var(--page-bg); position: relative; font-family: "Arimo", Arial, sans-serif; }

  .note {
    position: absolute;
    font-family: "Reenie Beanie", cursive;
    color: var(--note-ink);
    font-size: 40px;
    line-height: 1;
  }
  .note-front { left: 376px; top: 118px; }
  .note-back { left: 812px; top: 112px; }
  .note-or { left: 812px; top: 480px; font-size: 34px; }
  .note-arrow { position: absolute; }

  .card {
    position: absolute;
    width: 420px;
    height: 240px;
    background: var(--card-bg);
    border: 1px solid var(--card-edge);
    border-radius: 18px;
    overflow: hidden;
  }
  .card-front { left: 168px; top: 223px; }
  .card-back-pattern { left: 620px; top: 223px; }
  .card-back-plain { left: 620px; top: 526px; }

  /* front */
  .divider-line { position: absolute; left: 126px; top: 0; width: 2px; height: 240px; background: var(--ink-brown); }
  .brand-mark {
    position: absolute; left: 10px; bottom: 14px;
    font-size: 13px; color: var(--ink-brown); white-space: nowrap;
  }
  .art { position: absolute; background: var(--art-fill); }
  .art-floor-lamp { left: 137px; top: 12px; width: 86px; height: 106px; }
  .art-chair { left: 140px; top: 135px; width: 102px; height: 105px; }
  .art-pendant { left: 272px; top: 0; width: 130px; height: 122px; border-radius: 0 0 60px 60px; }

  .identity { position: absolute; left: 272px; top: 70px; width: 130px; text-align: center; color: var(--ink-brown); }
  .identity-name { font-size: 14px; color: var(--accent-orange); line-height: 17px; }
  .identity-role { font-size: 7px; line-height: 9px; }

  .contact { position: absolute; left: 271px; top: 133px; font-size: 8.5px; line-height: 12px; }
  .contact-row { display: flex; }
  .contact-row + .contact-row { margin-top: 16px; }
  .contact-row.tight { margin-top: 0; }
  .contact-label { width: 45px; color: var(--ink-brown); }
  .contact-value { color: var(--accent-orange); }

  /* back: pattern */
  .name-pattern {
    position: absolute; left: 0; top: 2px;
    font-family: "Oswald", sans-serif; font-weight: 300;
    font-size: 22px; line-height: 26px;
    color: var(--pattern-orange);
    white-space: nowrap;
  }
  .name-pattern .row { display: block; }
  .name-pattern .row.shifted { margin-left: -44px; }

  /* back: plain */
  .edge-line { position: absolute; top: 0; width: 2px; height: 240px; background: var(--ink-brown); }
  .edge-line.first { left: 34px; }
  .edge-line.second { left: 50px; }
  .wordmark {
    position: absolute; left: 145px; top: 102px;
    font-family: "Oswald", sans-serif; font-weight: 300;
    font-size: 26px; line-height: 30px;
    color: var(--ink-brown);
    border-bottom: 2px solid var(--accent-orange);
  }
</style>
</head>
<body>
  <div class="note note-front">front</div>
  <svg class="note-arrow" style="left:338px;top:138px" width="40" height="46" viewBox="0 0 40 46">
    <path d="M34 4 C24 16 16 28 10 40 M4 26 L10 41 L22 34" fill="none" stroke="#555" stroke-width="1.5" stroke-linecap="round"/>
  </svg>
  <div class="note note-back">back</div>
  <svg class="note-arrow" style="left:772px;top:132px" width="40" height="46" viewBox="0 0 40 46">
    <path d="M34 4 C24 16 16 28 10 40 M4 26 L10 41 L22 34" fill="none" stroke="#555" stroke-width="1.5" stroke-linecap="round"/>
  </svg>
  <div class="note note-or">or</div>

  <section class="card card-front" aria-label="Card front">
    <div class="divider-line"></div>
    <div class="brand-mark">lena vart spaces</div>
    <div class="art art-floor-lamp" role="img" aria-label="Line drawing of a tilted floor lamp"></div>
    <div class="art art-chair" role="img" aria-label="Line drawing of a tilted bistro chair"></div>
    <div class="art art-pendant" role="img" aria-label="Line drawing of a pendant lamp framing the name"></div>
    <div class="identity">
      <div class="identity-name">Lena Vart</div>
      <div class="identity-role">Interior Designer</div>
      <div class="identity-role">allied member, NPDG</div>
    </div>
    <div class="contact">
      <div class="contact-row"><span class="contact-label">address</span><span class="contact-value">4213 Willowmere Lane<br>Linden Falls, MN 55990</span></div>
      <div class="contact-row"><span class="contact-label">phone</span><span class="contact-value">612-555-0187</span></div>
      <div class="contact-row"><span class="contact-label">mail</span><span class="contact-value">lenapvart@orbimail.test</span></div>
      <div class="contact-row tight"><span class="contact-label">web</span><span class="contact-value">lenavartspaces.test</span></div>
    </div>
  </section>

  <section class="card card-back-pattern" aria-label="Card back, repeated name">
    <div class="name-pattern">
      <span class="row">lena vart spaces&nbsp;&nbsp;lena vart spaces&nbsp;&nbsp;lena vart spaces&nbsp;&nbsp;lena vart spaces</span>
      <span class="row shifted">lena vart spaces&nbsp;&nbsp;lena vart spaces&nbsp;&nbsp;lena vart spaces&nbsp;&nbsp;lena vart spaces</span>
      <span class="row">lena vart spaces&nbsp;&nbsp;lena vart spaces&nbsp;&nbsp;lena vart spaces&nbsp;&nbsp;lena vart spaces</span>
      <span class="row shifted">lena vart spaces&nbsp;&nbsp;lena vart spaces&nbsp;&nbsp;lena vart spaces&nbsp;&nbsp;lena vart spaces</span>
      <span class="row">lena vart spaces&nbsp;&nbsp;lena vart spaces&nbsp;&nbsp;lena vart spaces&nbsp;&nbsp;lena vart spaces</span>
      <span class="row shifted">lena vart spaces&nbsp;&nbsp;lena vart spaces&nbsp;&nbsp;lena vart spaces&nbsp;&nbsp;lena vart spaces</span>
      <span class="row">lena vart spaces&nbsp;&nbsp;lena vart spaces&nbsp;&nbsp;lena vart spaces&nbsp;&nbsp;lena vart spaces</span>
      <span class="row shifted">lena vart spaces&nbsp;&nbsp;lena vart spaces&nbsp;&nbsp;lena vart spaces&nbsp;&nbsp;lena vart spaces</span>
      <span class="row">lena vart spaces&nbsp;&nbsp;lena vart spaces&nbsp;&nbsp;lena vart spaces&nbsp;&nbsp;lena vart spaces</span>
    </div>
  </section>

  <section class="card card-back-plain" aria-label="Card back, plain">
    <div class="edge-line first"></div>
    <div class="edge-line second"></div>
    <div class="wordmark">lena vart spaces</div>
  </section>
</body>
</html>
```